Shop Window Desgin

I have a big glass window (office), 280cm wide by 302cm high and I want designing an advert for our property management business.

Our main colours are in the proeprty management logo attached. I have also uploaded a photo of the shop front (left window), please take into consideration the door.

I want the following text items placed:

PROPERTY MANAGEMENT
HOLIDAY RENTALS
KEYHOLDING
MARKETING & RESERVATIONS
GARDEN & POOL MAINTENACE
CLEANING & LAUNDRY

```html
<!DOCTYPE html>
<html lang="en">
<head>
<meta charset="utf-8">
<title>Harbour Property Management – Window Advert</title>
<link href="https://fonts.googleapis.com/css2?family=Montserrat:wght@600;700;800&family=Raleway:wght@500;700&display=swap" rel="stylesheet">
<style>
  :root {
    --orange: #e77f24;
    --grey: #7a7a7a;
    --grey-dark: #3f3f41;
    --paper: #ffffff;
    --mist: #f1f1f1;
    --badge-blue: #1c9ad6;
    --badge-purple: #4b3a5e;
    --frame: #111111;
  }
  html, body {
    margin: 0;
    padding: 0;
    width: 1091px;
    height: 1200px;
    overflow: hidden;
    background: var(--paper);
  }
  .window-advert {
    position: relative;
    width: 1091px;
    height: 1200px;
    overflow: hidden;
    background: linear-gradient(120deg, #ececec 0%, #f7f7f7 35%, #ffffff 70%);
    font-family: "Montserrat", sans-serif;
  }
  .brand {
    position: absolute;
    left: 95px;
    top: 66px;
    display: flex;
    align-items: center;
    gap: 20px;
  }
  .brand-dot {
    width: 176px;
    height: 176px;
    border-radius: 50%;
    background: var(--orange);
  }
  .brand-name {
    display: block;
    overflow: visible;
  }
  .brand-name text {
    font-family: "Montserrat", sans-serif;
    font-weight: 800;
    fill: var(--orange);
  }
  .services {
    position: absolute;
    left: 0;
    top: 0;
    margin: 0;
    padding: 0;
    list-style: none;
  }
  .service {
    position: absolute;
    left: 138px;
    width: 640px;
    height: 96px;
    display: flex;
    align-items: center;
  }
  .service-icon {
    position: relative;
    width: 94px;
    height: 94px;
    border-radius: 50%;
    background: radial-gradient(circle at 40% 35%, #ffffff 0%, #ececec 60%, #d4d4d4 100%);
    box-shadow: 0 3px 6px rgba(0,0,0,0.12);
    flex: none;
  }
  .service-icon::before {
    content: "";
    position: absolute;
    inset: -8px;
    border-radius: 50%;
    border: 1px dashed var(--orange);
    clip-path: inset(0 50% 0 0);
  }
  .service-icon::after {
    content: "";
    position: absolute;
    left: 46px;
    top: 94px;
    height: 20px;
    border-left: 1px dashed var(--orange);
  }
  .service:last-child .service-icon::after { display: none; }
  .service-name {
    margin: 0 0 0 25px;
    font-weight: 700;
    font-size: 30px;
    line-height: 36px;
    letter-spacing: 1px;
    color: var(--grey-dark);
  }
  .motif-right {
    position: absolute;
    left: 580px;
    top: 250px;
    width: 511px;
    height: 670px;
    border-radius: 180px 0 0 180px;
    background: radial-gradient(circle at 55% 45%, rgba(231,127,36,0.55) 0%, rgba(231,127,36,0.25) 45%, rgba(122,122,122,0.18) 75%, rgba(255,255,255,0) 100%);
  }
  .motif-left {
    position: absolute;
    left: 0;
    top: 816px;
    width: 130px;
    height: 384px;
    border-radius: 0 120px 0 0;
    background: linear-gradient(160deg, rgba(122,122,122,0.35) 0%, rgba(231,127,36,0.45) 60%, rgba(231,127,36,0.2) 100%);
  }
  .door-frame {
    position: absolute;
    left: 675px;
    top: 457px;
    width: 416px;
    height: 743px;
    border: 1px solid var(--frame);
    border-right: none;
    border-bottom: none;
    box-sizing: border-box;
  }
  .door-frame-inner {
    position: absolute;
    left: 684px;
    top: 468px;
    width: 398px;
    height: 722px;
    border: 1.5px solid var(--frame);
    box-sizing: border-box;
  }
  .badge-pool {
    position: absolute;
    left: 124px;
    top: 1028px;
    width: 96px;
    height: 96px;
    border-radius: 20px;
    background: var(--badge-blue);
    border: 4px solid #0d3f7a;
    transform: rotate(45deg) scale(0.9, 0.9);
  }
  .badge-association {
    position: absolute;
    left: 275px;
    top: 1040px;
    width: 324px;
    height: 78px;
    border-radius: 8px;
    background: linear-gradient(90deg, var(--badge-purple) 0%, #6a5a7c 75%, #d51c5b 100%);
    opacity: 0.85;
  }
  .web-address {
    position: absolute;
    left: 725px;
    top: 1081px;
    width: 315px;
    height: 33px;
    border-radius: 17px;
    background: var(--orange);
    color: var(--paper);
    font-family: "Raleway", sans-serif;
    font-weight: 500;
    font-size: 18px;
    line-height: 33px;
    text-align: center;
    letter-spacing: 0.3px;
  }
  .web-address strong { font-weight: 700; }
</style>
</head>
<body>
<main class="window-advert">
  <div class="motif-right" role="img" aria-label="Large interlaced orange and grey brand ribbon decoration"></div>
  <div class="motif-left" role="img" aria-label="Orange and grey ribbon decoration curving in from the left edge"></div>

  <header class="brand">
    <span class="brand-dot"></span>
    <svg class="brand-name" width="480" height="158" viewBox="0 0 480 158" aria-label="Harbour Property Management">
      <text x="0" y="106" font-size="112" textLength="478" lengthAdjust="spacingAndGlyphs">HARBOUR</text>
      <text x="0" y="158" font-size="44" textLength="478" lengthAdjust="spacingAndGlyphs">PROPERTY MANAGEMENT</text>
    </svg>
  </header>

  <ul class="services">
    <li class="service" style="top:298px"><span class="service-icon" role="img" aria-label="Buildings icon"></span><h2 class="service-name">PROPERTY<br>MANAGEMENT</h2></li>
    <li class="service" style="top:413px"><span class="service-icon" role="img" aria-label="Palm island icon"></span><h2 class="service-name">HOLIDAY<br>RENTALS</h2></li>
    <li class="service" style="top:527px"><span class="service-icon" role="img" aria-label="Key handover icon"></span><h2 class="service-name">KEYHOLDING</h2></li>
    <li class="service" style="top:642px"><span class="service-icon" role="img" aria-label="Connected customers icon"></span><h2 class="service-name">MARKETING &amp;<br>RESERVATIONS</h2></li>
    <li class="service" style="top:756px"><span class="service-icon" role="img" aria-label="Swimming pool ladder icon"></span><h2 class="service-name">GARDEN &amp;<br>POOL MAINTENACE</h2></li>
    <li class="service" style="top:871px"><span class="service-icon" role="img" aria-label="Washing machine icon"></span><h2 class="service-name">CLEANING &amp;<br>LAUNDRY</h2></li>
  </ul>

  <div class="badge-pool" role="img" aria-label="Pool operator certification badge"></div>
  <div class="badge-association" role="img" aria-label="Rental management association membership badge"></div>

  <div class="door-frame"></div>
  <div class="door-frame-inner"></div>

  <p class="web-address" style="margin:0">www.<strong>HarbourProperty</strong>.com</p>
</main>
</body>
</html>
```